Advertisements for dental office (3"x3.75" and 3"x2")
People of all ages looking for a family dentist.
I am looking for advertisements that are clean and sophisticated. Most dental ads are cluttered looking and list all the procedures that a dentist will perform. I do not want clutter. I want an ad that speaks for itself and has a lot of emotional appeal. The ads should be simple but still catch your eye.

```html
<!DOCTYPE html>
<html lang="en">
<head>
<meta charset="utf-8">
<title>Martin T. Revell, DDS – Family Dentistry Ad</title>
<link rel="stylesheet" href="https://fonts.googleapis.com/css2?family=Marcellus+SC&family=Crimson+Text:ital,wght@1,400;1,600;1,700&family=Open+Sans:wght@400;700&display=swap">
<style>
  :root {
    --stage: #4a2b20;
    --paper: #ffffff;
    --paper-shade: #eeeceb;
    --plum: #8c1a4c;
    --plum-deep: #5e0d33;
    --plum-bright: #b0286a;
    --ink: #3a3236;
    --ink-soft: #4d4548;
    --photo-warm: #b88a6e;
    --photo-dark: #5a3a2c;
  }
  html, body {
    margin: 0;
    width: 1200px;
    height: 956px;
    overflow: hidden;
    background: var(--stage);
  }
  .ad {
    position: absolute;
    left: 96px;
    top: 70px;
    width: 1004px;
    height: 812px;
    background: linear-gradient(180deg, var(--paper) 0%, var(--paper) 70%, var(--paper-shade) 100%);
    box-shadow: 0 6px 22px rgba(0,0,0,.45);
    overflow: hidden;
  }
  .ad__photo {
    position: absolute;
    left: 0;
    top: 0;
    width: 660px;
    height: 812px;
    background:
      radial-gradient(ellipse 42% 38% at 38% 50%, rgba(232,190,160,.9) 0%, rgba(232,190,160,0) 100%),
      linear-gradient(90deg, var(--photo-dark) 0%, var(--photo-warm) 45%, rgba(255,255,255,0) 100%);
  }
  .ad__banner {
    position: absolute;
    left: 18px;
    top: 13px;
    width: 948px;
    height: 54px;
    border-radius: 0 27px 27px 0;
    background: linear-gradient(90deg, var(--plum-deep) 0%, var(--plum-bright) 45%, var(--plum) 100%);
    display: flex;
    align-items: center;
    padding-left: 104px;
    box-sizing: border-box;
    color: var(--paper);
    font-family: "Marcellus SC", serif;
    font-size: 30px;
    letter-spacing: 2px;
    white-space: nowrap;
  }
  .ad__text {
    position: absolute;
    left: 570px;
    width: 400px;
    margin: 0;
    text-align: center;
    white-space: nowrap;
  }
  .ad__lead {
    top: 112px;
    font-family: "Crimson Text", serif;
    font-style: italic;
    font-weight: 600;
    font-size: 58px;
    line-height: 60px;
    color: var(--plum);
  }
  .ad__headline {
    top: 180px;
    font-family: "Crimson Text", serif;
    font-style: italic;
    font-weight: 700;
    font-size: 104px;
    line-height: 110px;
    color: var(--plum);
  }
  .ad__tagline {
    top: 306px;
    font-family: "Crimson Text", serif;
    font-style: italic;
    font-weight: 600;
    font-size: 46px;
    line-height: 58px;
    color: var(--ink);
  }
  .ad__brand {
    top: 560px;
    display: flex;
    justify-content: center;
    align-items: center;
    gap: 12px;
    font-family: "Marcellus SC", serif;
    font-size: 36px;
    line-height: 48px;
    color: var(--plum);
  }
  .ad__brand-dot {
    width: 20px;
    height: 20px;
    border-radius: 50%;
    background: var(--plum);
  }
  .ad__practice {
    top: 652px;
    left: 566px;
    width: 408px;
    padding-bottom: 4px;
    border-bottom: 2px solid var(--plum);
    font-family: "Marcellus SC", serif;
    font-size: 27px;
    line-height: 34px;
    color: var(--plum);
  }
  .ad__address {
    top: 696px;
    font-family: "Open Sans", sans-serif;
    font-size: 22px;
    line-height: 30px;
    color: var(--ink-soft);
  }
  .ad__phone {
    top: 745px;
    font-family: "Open Sans", sans-serif;
    font-weight: 700;
    font-size: 23px;
    line-height: 30px;
    color: var(--ink);
  }
</style>
</head>
<body>
  <section class="ad">
    <div class="ad__photo" role="img" aria-label="Portrait photo of a smiling young woman with long brown hair blowing softly, fading into white"></div>
    <div class="ad__banner">Comprehensive Dentistry For All Ages</div>
    <p class="ad__text ad__lead">A Beautiful</p>
    <h1 class="ad__text ad__headline">Smile</h1>
    <p class="ad__text ad__tagline">Today, It's Easier<br>Than Ever</p>
    <div class="ad__text ad__brand"><span class="ad__brand-dot"></span>Revell Dental</div>
    <p class="ad__text ad__practice">Martin T. Revell, DDS, PLLC</p>
    <p class="ad__text ad__address">218 West Alder Street, Millbrook</p>
    <p class="ad__text ad__phone">Call us: 555-014-2368</p>
  </section>
</body>
</html>
```